Bref créative
RL Advisory
I need double sided standard sized Business Card [3.5" x 2"]
Use same font as in logo...also can mix it up with complimentary font
Professional
Romy Lindqvist, MBA, ACC
Nashville, TN
rl@romylindqvist-demo.com
www.romylindqvist-demo.com
please add twitter account underneath email address
Twitter: @RLpathways
Symbol only in the middle of the back of card.
with website address noted again underneath the symbol (www.romylindqvist-demo.com)

```html
<!DOCTYPE html>
<html lang="en">
<head>
<meta charset="utf-8">
<title>RL Advisory – Business Cards</title>
<link rel="stylesheet" href="https://fonts.googleapis.com/css2?family=Questrial&family=Arimo&display=swap">
<style>
  :root {
    --wine: #6a0b0e;
    --wine-text: #8a1c1f;
    --ink: #1a1a1a;
    --paper: #ffffff;
    --edge: #c9c9c9;
    --grey-light: #f4f4f4;
    --grey-dark: #a6a6a6;
  }
  * { margin: 0; padding: 0; box-sizing: border-box; }
  html, body { width: 1200px; height: 713px; overflow: hidden; background: var(--paper); }
  .sheet { position: relative; width: 1200px; height: 713px; }

  .card {
    position: absolute;
    width: 552px; height: 312px;
    overflow: hidden;
    border: 1px solid var(--edge);
    background: var(--paper);
  }
  .card--front { left: 24px; top: 29px; }
  .card--back-white { left: 612px; top: 29px; }
  .card--back-wine { left: 24px; top: 367px; background: var(--wine); border-color: var(--wine); }
  .card--back-grey { left: 612px; top: 367px; background: radial-gradient(ellipse at center, var(--grey-light) 0%, #d6d6d6 55%, var(--grey-dark) 100%); }

  .front-sweep { position: absolute; inset: 0; }

  .mark-dot { position: absolute; border-radius: 50%; background: var(--wine); }
  .brand-name {
    position: absolute;
    font-family: "Questrial", sans-serif;
    font-weight: 400;
    color: var(--ink);
    white-space: nowrap;
  }
  .brand-tagline {
    position: absolute;
    font-family: "Arimo", sans-serif;
    font-weight: 700;
    color: var(--wine-text);
    white-space: nowrap;
  }

  /* front */
  .card--front .mark-dot { left: 104px; top: 16px; width: 56px; height: 56px; }
  .card--front .brand-name { left: 22px; top: 96px; font-size: 34px; }
  .card--front .brand-tagline { left: 60px; top: 140px; font-size: 10px; }
  .holder-name {
    position: absolute; left: 70px; top: 170px;
    font-family: "Arimo", sans-serif; font-size: 20px; color: var(--wine-text);
  }
  .contact {
    position: absolute; left: 22px; top: 218px;
    list-style: none;
    font-family: "Arimo", sans-serif; font-size: 12.5px; line-height: 16px; color: var(--ink);
  }
  .contact .web { color: var(--wine-text); }

  /* backs */
  .back-center { position: absolute; left: 0; width: 100%; text-align: center; }
  .back-mark { top: 62px; }
  .back-mark .mark-dot { position: relative; display: inline-block; width: 84px; height: 84px; }
  .back-name { top: 160px; font-family: "Questrial", sans-serif; font-size: 44px; color: var(--ink); }
  .back-tagline { top: 212px; font-family: "Arimo", sans-serif; font-weight: 700; font-size: 12px; color: var(--wine-text); padding-left: 60px; }
  .back-web { top: 252px; font-family: "Arimo", sans-serif; font-size: 14px; color: var(--ink); }

  .card--back-wine .mark-dot { background: var(--paper); }
  .card--back-wine .back-name,
  .card--back-wine .back-tagline { color: var(--paper); }
  .card--back-wine .back-mark { top: 78px; }
  .card--back-wine .back-name { top: 176px; }
  .card--back-wine .back-tagline { top: 228px; }
</style>
</head>
<body>
<main class="sheet">

  <section class="card card--front" aria-label="Card front">
    <svg class="front-sweep" width="552" height="312" viewBox="0 0 552 312" aria-hidden="true">
      <path d="M415 0 Q 480 150 520 312 L552 312 L552 0 Z" fill="var(--wine)"/>
    </svg>
    <span class="mark-dot" aria-hidden="true"></span>
    <span class="brand-name">RL Advisory</span>
    <span class="brand-tagline">Career and Workforce Solutions</span>
    <p class="holder-name">Romy Lindqvist, MBA, ACC</p>
    <ul class="contact">
      <li>Nashville, TN</li>
      <li>Phone: 615.555.0142</li>
      <li>Email: rl@romylindqvist-demo.com</li>
      <li>Twitter: @RLpathways</li>
      <li class="web">www.romylindqvist-demo.com</li>
    </ul>
  </section>

  <section class="card card--back-white" aria-label="Card back, white">
    <div class="back-center back-mark"><span class="mark-dot" aria-hidden="true"></span></div>
    <p class="back-center back-name">RL Advisory</p>
    <p class="back-center back-tagline">Career and Workforce Solutions</p>
    <p class="back-center back-web">www.romylindqvist-demo.com</p>
  </section>

  <section class="card card--back-wine" aria-label="Card back, wine">
    <div class="back-center back-mark"><span class="mark-dot" aria-hidden="true"></span></div>
    <p class="back-center back-name">RL Advisory</p>
    <p class="back-center back-tagline">Career and Workforce Solutions</p>
  </section>

  <section class="card card--back-grey" aria-label="Card back, grey">
    <div class="back-center back-mark"><span class="mark-dot" aria-hidden="true"></span></div>
    <p class="back-center back-name">RL Advisory</p>
    <p class="back-center back-tagline">Career and Workforce Solutions</p>
    <p class="back-center back-web">www.romylindqvist-demo.com</p>
  </section>

</main>
</body>
</html>
```